The Steel Hand Close Quarters Protocol Cover

Hi we are producing a self defense course entitled The Steel Hand Close Quarters Protocol: A Complete Field Manual For Commanding The Blade Every Operator Trusts Above Any Other Tool.

I listed this as a book cover but it will actually be a DVD set, but the book cover model works fine.

See below for design examples - I am thinking we need a cover that will appeal to military/survival type people.

Target Market(s)

survivalists, cops, preppers, gun owners, martial artists, and average people wanting to learn how to defend themselves

Industry/Entity Type

Defense

Requirements
Must have
• Title: THE STEEL HAND CLOSE QUARTERS PROTOCOL: A COMPLETE FIELD MANUAL FOR COMMANDING THE BLADE EVERY OPERATOR TRUSTS ABOVE ANY OTHER TOOL
Nice to have
• Please look at these sample designs from other books as a model:
• https://files.pelorvane-archive.example/covers/4/27/MarlowGrayfield.jpg - This stye is ideal.
• Other good examples:
• https://media2.quillorbit.example/8841027_k390.jpg
• http://c.tovenreads.example/titles/1289045517m/48102936.jpg
• http://img.brisketmart.example/pics/P/73Rt82MqWnB._XZ_QT410_LM305,410_.jpg
• http://3.cdn.jottlepage.example/-MRtYVVKDDQ/BWNs_harpoQ/BBBBBBBBx9K/TRPk418WpXZ/s1600/Q3408817.JPG

```html
<!DOCTYPE html>
<html lang="en">
<head>
<meta charset="utf-8">
<title>The Steel Hand Close Quarters Protocol</title>
<link rel="stylesheet" href="https://fonts.googleapis.com/css2?family=Stardos+Stencil:wght@400;700&family=Oswald:wght@400;500&display=swap">
<style>
  :root {
    --olive-deep: #4f6a1a;
    --olive-mid: #7f9a2c;
    --olive-light: #b3c244;
    --title-white: #f1f2ea;
    --band-dark: #34431a;
    --band-text: #e9edd9;
    --ink: #16170f;
    --blade-dark: #1d1f1c;
    --blade-mid: #3a3d37;
  }
  html, body {
    margin: 0;
    padding: 0;
    width: 841px;
    height: 1200px;
    overflow: hidden;
  }
  .cover {
    position: relative;
    width: 841px;
    height: 1200px;
    overflow: hidden;
    background:
      radial-gradient(ellipse 520px 700px at 560px 560px, var(--olive-light) 0%, rgba(179,194,68,0) 75%),
      radial-gradient(ellipse 900px 900px at 420px 600px, var(--olive-mid) 0%, var(--olive-deep) 100%);
  }
  .knife-visual {
    position: absolute;
    left: 648px;
    top: 0;
    width: 140px;
    height: 1200px;
    z-index: 1;
    background: linear-gradient(90deg, var(--blade-mid) 0%, var(--blade-dark) 55%, var(--blade-mid) 100%);
  }
  .title {
    position: absolute;
    left: 0;
    top: 0;
    width: 630px;
    height: 800px;
    z-index: 2;
    overflow: hidden;
  }
  .title text {
    font-family: "Stardos Stencil", "Impact", sans-serif;
    font-weight: 700;
    fill: var(--title-white);
  }
  .subtitle {
    position: absolute;
    left: 0;
    top: 818px;
    width: 684px;
    margin: 0;
    z-index: 2;
    text-align: center;
    font-family: "Oswald", "Arial Narrow", sans-serif;
    font-weight: 500;
    font-size: 33px;
    letter-spacing: 4px;
    line-height: 53px;
  }
  .subtitle span {
    display: inline-block;
    padding: 0 8px;
    line-height: 44px;
    color: var(--ink);
  }
  .subtitle .band {
    background: var(--band-dark);
    color: var(--band-text);
  }
  .author {
    position: absolute;
    left: 0;
    top: 1080px;
    width: 684px;
    margin: 0;
    z-index: 2;
    text-align: center;
    font-family: "Stardos Stencil", "Impact", sans-serif;
    font-weight: 700;
    font-size: 50px;
    letter-spacing: 2px;
    color: var(--ink);
  }
</style>
</head>
<body>
  <main class="cover">
    <div class="knife-visual" role="img" aria-label="Upright black combat knife with serrated spine and ribbed handle"></div>

    <svg class="title" viewBox="0 0 630 800" xmlns="http://www.w3.org/2000/svg" aria-label="The Steel Hand Close Quarters Protocol">
      <text x="130" y="96" font-size="100" textLength="380" lengthAdjust="spacingAndGlyphs">THE STEEL</text>
      <text x="52" y="300" font-size="260" textLength="536" lengthAdjust="spacingAndGlyphs">HAND</text>
      <text x="56" y="414" font-size="128" textLength="528" lengthAdjust="spacingAndGlyphs">CLOSE</text>
      <text x="130" y="504" font-size="86" textLength="380" lengthAdjust="spacingAndGlyphs">QUARTERS</text>
      <text x="52" y="762" font-size="320" textLength="530" lengthAdjust="spacingAndGlyphs">PROTOCOL</text>
    </svg>

    <p class="subtitle">
      <span class="band">A COMPLETE FIELD MANUAL</span><br>
      <span>FOR COMMANDING THE BLADE</span><br>
      <span class="band">EVERY OPERATOR TRUSTS</span><br>
      <span class="band">ABOVE ANY OTHER</span><br>
      <span>TOOL</span>
    </p>

    <p class="author">GRANT R HOLLIS</p>
  </main>
</body>
</html>
```